Business Card Design Project for - The Brackenfold Lawncare Company Ltd. We are a Landscape and garden

I would like designer to use all special glosses etc so i can have a professional looking business card. The theme of the business card can reflect that of the Logo attached by ArtVellum or your own unique ideas.. please feel free to go wild as i hope i can select a winner i like - my budget will be committed so please get involved. Good luck and thank you Neville

Target Market(s)

Must look Professional

General Public and Businesses including Councils, Local Government, Hospitals, Hotels, Professionals and Professional Sports People.

Industry/Entity Type

Landscape Gardening

Contact Information for Business Card

The Brackenfold Lawncare Company Ltd

Mr R.P Ashworth
Head Office - Quayline Park Manchester
t. 0772 458 916
e. info@brackenfoldlawn.co.uk
w. www.brackenfoldlawn.co.uk

Facebook - https://www.pagemural.com/TheBrackenfoldLawncareCompany/
Twitter - https://chirpline.com/ThePlotTruck
Instagram - https://www.snapquilt.com/thebrackenfoldlawncarecompany/?hl=en
Google+ - https://circles.vondarix.com/u/0/208475932610482739516
Yelp - https://www.localrava.co.uk/biz/the-brackenfold-lawncare-company-manchester-4

Font styles to use
Serif
Script
Other font styles liked:
• I don't have much of an idea of font types sorry

Colors

Designer to choose colors to be used in the design.

Requirements
Must have
• A Professional look and Design
• Special effects with gloss and fading of colours possibly..
• Front and back design
Nice to have
• All special features with effects and gloss etc

```html
<!DOCTYPE html>
<html lang="en">
<head>
<meta charset="utf-8">
<title>The Brackenfold Lawncare Company Ltd – Business Card</title>
<link rel="stylesheet" href="https://fonts.googleapis.com/css2?family=Tinos&family=Montserrat:wght@500&display=swap">
<style>
  :root {
    --page-bg: #f4f4f5;
    --navy-deep: #0b1230;
    --navy-mid: #111d40;
    --navy-light: #1e3a6b;
    --navy-ghost: #15244c;
    --silver-text: #a3a7b0;
    --leaf-green: #3f9b2f;
    --leaf-green-light: #8fd14f;
    --card-light-a: #c4c5c8;
    --card-light-b: #eef0f2;
    --card-border: #a6cfe2;
    --ink-navy: #1a2a52;
    --ghost-panel: rgba(255,255,255,0.28);
  }
  * { margin: 0; padding: 0; box-sizing: border-box; }
  html, body { width: 1200px; height: 1200px; overflow: hidden; }
  body {
    background: radial-gradient(circle at 50% 50%, #ffffff 0%, #ffffff 45%, var(--page-bg) 100%);
    position: relative;
  }
  .card {
    position: absolute;
    left: 253px;
    width: 697px;
    height: 398px;
    border-radius: 9px;
    overflow: hidden;
    box-shadow: 0 2px 6px rgba(0,0,0,0.12);
  }
  .card-gloss {
    position: absolute;
    inset: 0;
    pointer-events: none;
    background:
      linear-gradient(115deg, rgba(255,255,255,0) 38%, rgba(255,255,255,0.10) 52%, rgba(255,255,255,0) 66%),
      linear-gradient(180deg, rgba(255,255,255,0.08) 0%, rgba(255,255,255,0) 45%);
  }
  .card-back .card-gloss {
    background:
      linear-gradient(115deg, rgba(255,255,255,0) 30%, rgba(255,255,255,0.35) 48%, rgba(255,255,255,0) 62%);
  }

  /* Front */
  .card-front {
    top: 210px;
    background: linear-gradient(90deg, var(--navy-deep) 0%, var(--navy-mid) 55%, var(--navy-light) 82%, var(--navy-light) 100%);
  }
  .front-ghost-mark {
    position: absolute;
    left: 0; top: 15px;
    width: 320px; height: 340px;
    border-radius: 50%;
    background: radial-gradient(circle at 40% 40%, var(--navy-ghost) 0%, rgba(21,36,76,0.6) 60%, rgba(21,36,76,0) 72%);
  }
  .front-brand-dot {
    position: absolute;
    left: 425px; top: 52px;
    width: 150px; height: 150px;
    border-radius: 50%;
    background: radial-gradient(circle at 35% 30%, var(--leaf-green-light) 0%, var(--leaf-green) 55%, #2a7420 100%);
  }
  .brand-name {
    font-family: "Tinos", serif;
    font-weight: 400;
    text-transform: uppercase;
    white-space: nowrap;
  }
  .front-name {
    position: absolute;
    right: 17px;
    top: 232px;
    text-align: right;
    color: var(--silver-text);
  }
  .front-name .line-one { display: block; font-size: 38px; line-height: 44px; letter-spacing: 0.5px; }
  .front-name .line-two { display: block; font-size: 23px; line-height: 30px; margin-right: 28px; }

  /* Back */
  .card-back {
    top: 646px;
    background: linear-gradient(90deg, var(--card-light-a) 0%, #dcdee0 50%, var(--card-light-b) 100%);
    border: 1.5px solid var(--card-border);
  }
  .back-ghost-panel {
    position: absolute;
    left: 400px; top: 118px;
    width: 270px; height: 262px;
    border-radius: 36px 36px 10px 10px;
    background: var(--ghost-panel);
  }
  .back-brand-dot {
    position: absolute;
    left: 56px; top: 38px;
    width: 76px; height: 76px;
    border-radius: 50%;
    background: radial-gradient(circle at 35% 30%, var(--leaf-green-light) 0%, var(--leaf-green) 55%, #2a7420 100%);
  }
  .back-name {
    position: absolute;
    left: 160px;
    top: 40px;
    color: var(--ink-navy);
  }
  .back-name .line-one { display: block; font-size: 33px; line-height: 36px; letter-spacing: 0.5px; }
  .back-name .line-two { display: block; font-size: 22px; line-height: 28px; margin-left: 12px; }
  .contact-person {
    position: absolute;
    left: 173px;
    top: 114px;
    font-family: "Montserrat", sans-serif;
    font-weight: 500;
    font-size: 14px;
    letter-spacing: 1px;
    text-transform: uppercase;
    color: var(--ink-navy);
  }

  .contact-list {
    position: absolute;
    left: 30px;
    top: 158px;
    list-style: none;
    font-family: "Montserrat", sans-serif;
    font-weight: 500;
    font-size: 14px;
    color: var(--ink-navy);
    text-transform: uppercase;
  }
  .contact-item {
    display: flex;
    align-items: center;
    height: 40px;
  }
  .contact-item.tall { height: 52px; line-height: 19px; }
  .contact-icon { width: 24px; height: 24px; margin-right: 24px; flex: none; fill: var(--ink-navy); }
</style>
</head>
<body>

<section class="card card-front" aria-label="Business card front">
  <div class="front-ghost-mark" role="img" aria-label="Faint enlarged company emblem"></div>
  <div class="front-brand-dot" aria-hidden="true"></div>
  <h1 class="brand-name front-name">
    <span class="line-one">The Brackenfold</span>
    <span class="line-two">Lawncare Company Ltd</span>
  </h1>
  <div class="card-gloss" aria-hidden="true"></div>
</section>

<section class="card card-back" aria-label="Business card back">
  <div class="back-ghost-panel" role="img" aria-label="Faint patterned company emblem"></div>
  <div class="back-brand-dot" aria-hidden="true"></div>
  <h2 class="brand-name back-name">
    <span class="line-one">The Brackenfold</span>
    <span class="line-two">Lawncare Company Ltd</span>
  </h2>
  <p class="contact-person">Mr R.P Ashworth</p>

  <ul class="contact-list">
    <li class="contact-item">
      <svg class="contact-icon" viewBox="0 0 24 24" aria-hidden="true"><path d="M6.6 10.8c1.4 2.8 3.8 5.1 6.6 6.6l2.2-2.2c.3-.3.7-.4 1-.2 1.1.4 2.3.6 3.6.6.6 0 1 .4 1 1V20c0 .6-.4 1-1 1C10.6 21 3 13.4 3 4c0-.6.4-1 1-1h3.5c.6 0 1 .4 1 1 0 1.3.2 2.5.6 3.6.1.3 0 .7-.2 1z"/></svg>
      <span>0772 458 916</span>
    </li>
    <li class="contact-item">
      <svg class="contact-icon" viewBox="0 0 24 24" aria-hidden="true"><text x="12" y="19" text-anchor="middle" font-family="Montserrat, sans-serif" font-size="22" font-weight="700">@</text></svg>
      <span>info@brackenfoldlawn.co.uk</span>
    </li>
    <li class="contact-item tall">
      <svg class="contact-icon" viewBox="0 0 24 24" aria-hidden="true"><path d="M10 20v-6h4v6h5v-8h3L12 3 2 12h3v8z"/></svg>
      <span>Head Office, Quayline Park,<br>Manchester</span>
    </li>
    <li class="contact-item">
      <svg class="contact-icon" viewBox="0 0 24 24" aria-hidden="true"><g fill="none" stroke="#1a2a52" stroke-width="1.8"><circle cx="12" cy="12" r="9.5"/><ellipse cx="12" cy="12" rx="4.2" ry="9.5"/><line x1="2.5" y1="12" x2="21.5" y2="12"/><path d="M4.5 7h15M4.5 17h15"/></g></svg>
      <span>www.brackenfoldlawn.co.uk</span>
    </li>
    <li class="contact-item">
      <svg class="contact-icon" viewBox="0 0 24 24" aria-hidden="true"><rect x="3" y="3" width="18" height="18" rx="2"/></svg>
      <span>followbrackenfold</span>
    </li>
  </ul>
  <div class="card-gloss" aria-hidden="true"></div>
</section>

</body>
</html>
```